2026 Compostable Stand up Pouch Redesign

Project Overview
We are a natural dog bakery focused on simple, healthy ingredients and earth-friendly packaging. As the first step in a rebrand, we are redesigning our 6 oz stand-up pouch using new compostable packaging materials.
New pouch is the same size and structure as current (template provided)
Files included:
Existing Art template (PDF + JPG)
Photos of current packaging (for reference only)
Copy of existing logo (Meadowlark Treat Kitchen)
Copy of future logo (Birchwood Natural Bakery)
This redesign should feel like a clear upgrade—more refined, more intentional, and more aligned with sustainability.
⚠️ IMPORTANT LAYOUT CONSTRAINT (PLEASE READ)
The new pouch has a full-width horizontal window.
Design elements may ONLY appear above and below the window
No design elements can be placed to the left or right of the window
A 4.5" W x 3.5" H blank space above the window must be preserved
This is reserved for applied product labels
Keep this area completely clean (no textures, patterns, or graphics)
Submissions that ignore these elements will not be considered.
Brand Direction & Style
We are looking for a design that feels:
Natural and ingredient-focused
Eco-conscious and sustainable
Clean and elevated (not rustic, not overly playful)
Warm and trustworthy
Avoid:
Neon or bright artificial colors
Loud, busy, or overly commercial designs
Cartoon-heavy or overly whimsical styles
Color Direction
Our current packaging is kraft brown, but the new material allows full-color printing. We are looking for:
Nature-inspired colors only
Greens, muted blues, warm browns, soft earth tones
Background color is flexible within this palette
Must work with:
Current logo: Meadowlark Treat Kitchen
Future logo: Birchwood Natural Bakery
👉 For this project, use Meadowlark Treat Kitchen logo only
Front of Pouch Requirements
Do NOT include logo on pouch front
(Logo will be on applied labels)
Required Elements
Tagline: Simple, Healthy Ingredients. Earth Friendly Packaging.
Compostable Messaging (REQUIRED):
Must clearly communicate that packaging is compostable
Optional placement:
Tear-off strip near hang hole
BUT must also appear somewhere on the main pouch design
Origin Callout:
“Hand Made in the Pacific Northwest”
Can be a badge, stamp, or graphic (open to redesign)
Icons (Highly Encouraged)
We would like to explore a clean, minimal icon set for:
No Corn
No Wheat
No Soy
No GMOs
Compostable Packaging
(Keep icons simple, clean, and consistent with natural aesthetic)
Back of Pouch Requirements
Messaging Direction
Do NOT use: “The healthiest pet bakery in the US”
Instead, build around:
Simple, Healthy Ingredients. Earth Friendly Packaging.
Content
“Our Recipes” bullet points (from current packaging – still valid)
Sustainability messaging:
Include reference to reducing our “carbon pawprint”
Emphasize eco-friendly materials and practices
Design Direction
Open to new layout and graphics
Should visually reinforce:
Clean ingredients
Natural sourcing
Sustainability
Printing Considerations
Design should be mindful of production scalability:
Should translate well to both digital and roto printing
Avoid overly complex gradients or excessive color layering
Creative Freedom (Important)
While we have outlined structure and constraints, we are intentionally leaving visual interpretation open.
We welcome:
Fresh layout ideas
Refined graphic elements
Elevated visual storytelling
We are especially interested in designs that feel:
Thoughtful
Clean
Naturally premium
Any design submission that includes loud, neon, or "aggressive" color schemes or a mass market appeal will be eliminated immediately. We are a premium, natural dog bakery found in independent stores only.
UPDATED & IMPORTANT DESIGN REQUIREMENTS (PLEASE READ)
This pouch is a base design used across all flavors. A separate product label will be applied.
A clearly defined blank area must be left for label placement (do not incorporate into artwork).
The product viewing window is fixed:
Size and placement must match the template exactly
Do not resize, reposition, or redesign the window
Designs that do not follow these requirements will not be considered.
Please review the discussion board for additional feedback and direction before submitting revisions.

```html
<!DOCTYPE html>
<html lang="en">
<head>
<meta charset="utf-8">
<title>Compostable Pouch – Front &amp; Back</title>
<link href="https://fonts.googleapis.com/css2?family=Lilita+One&family=Outfit:wght@300;400&display=swap" rel="stylesheet">
<style>
:root{
  --sage:#c0c9a1;
  --sage-deep:#a9b995;
  --teal:#5a9190;
  --olive:#8a9a6e;
  --line:#eef0dc;
  --stage:#92999d;
  --bar:#7a7f84;
  --head:"Lilita One", sans-serif;
  --body:"Outfit", sans-serif;
}
*{margin:0;padding:0;box-sizing:border-box}
html,body{width:1200px;height:976px;overflow:hidden}
body{background:var(--stage);position:relative;font-family:var(--body)}
.palette-bar{position:absolute;left:0;top:0;width:1200px;height:88px;background:var(--bar);color:#fff}
.palette-title{position:absolute;left:450px;top:25px;font-size:16px;letter-spacing:.5px}
.swatch{position:absolute;top:25px;width:50px;height:20px}
.swatch-code{position:absolute;top:52px;font-size:12px;width:70px;text-align:center}
.view-label{position:absolute;top:101px;color:#fff;font-size:16px;letter-spacing:.5px}
.pouch{position:absolute;top:125px;width:517px;height:793px;background:var(--sage);border:1px solid var(--line);border-radius:17px;overflow:hidden}
.pouch-frame{position:absolute;inset:0}

/* front */
.tagline{position:absolute;top:130px;left:0;width:517px;display:flex;align-items:center;justify-content:center;color:var(--teal);font-family:var(--head);line-height:.92}
.tag-item{text-align:center;padding:0 9px}
.tag-item + .tag-item{border-left:1px dashed var(--teal)}
.tag-simple{font-size:27px}
.tag-big{font-size:29px}
.tag-small{font-size:18px}
.label-window{position:absolute;left:104px;top:527px;width:310px;height:111px;background:#fff;border-radius:8px}
.free-from{position:absolute;top:654px;left:144px;display:flex}
.free-item{width:57px;text-align:center;color:var(--teal);font-size:12px;line-height:17px}
.free-item + .free-item{border-left:1px dashed var(--teal)}
.free-icon{display:block;margin:4px auto 8px}

/* back */
.recipes-head{position:absolute;left:74px;top:145px;width:152px;height:81px;background:var(--olive);color:var(--sage);font-family:var(--head);font-size:31px;line-height:33px;text-align:center;padding-top:8px}
.recipe-list{position:absolute;left:52px;top:238px;width:190px;list-style:none}
.recipe{display:flex;align-items:center;height:51px;border-bottom:1px dashed var(--teal);color:var(--teal);font-family:var(--head);font-size:13px;line-height:15.5px;margin-left:8px}
.recipe:last-child{border-bottom:none}
.recipe-icon{width:38px;height:32px;margin-right:16px;margin-left:-8px;flex:none}
.brand-name{position:absolute;left:272px;top:188px;width:215px;display:flex;align-items:center;gap:10px;color:var(--teal);font-family:var(--head);font-size:24px;line-height:26px}
.brand-dot{width:34px;height:34px;border-radius:50%;background:var(--teal);flex:none}
.badge{position:absolute;border-radius:50%;border:3px solid var(--teal);background:radial-gradient(circle at 50% 45%, var(--sage) 0%, var(--sage-deep) 55%, var(--teal) 130%)}
.badge-eco{left:306px;top:336px;width:142px;height:121px;background:radial-gradient(circle at 50% 45%, var(--sage) 0%, var(--sage-deep) 60%, var(--olive) 140%)}
.badge-origin{left:72px;top:452px;width:150px;height:145px}
.contact{position:absolute;left:263px;top:493px;width:225px;height:61px;border:1px dashed var(--teal);color:var(--teal);font-size:13.5px;line-height:16px;text-align:center;padding-top:6px;font-weight:300}
.eco-copy{position:absolute;left:40px;top:610px;width:437px;text-align:center;color:var(--teal);font-size:11.6px;line-height:17px;font-weight:300}
.compost{position:absolute;left:0;top:704px;width:517px;text-align:center;color:var(--olive);font-family:var(--head);line-height:1}
.compost-big{font-size:27px}
.compost-small{font-size:17px;margin-top:1px}
</style>
</head>
<body>
<header class="palette-bar">
  <span class="palette-title">PALETTE</span>
  <span class="swatch" style="left:537px;background:var(--sage)"></span>
  <span class="swatch" style="left:616px;background:var(--teal)"></span>
  <span class="swatch" style="left:696px;background:var(--olive)"></span>
  <span class="swatch-code" style="left:527px">#C0C9A1</span>
  <span class="swatch-code" style="left:606px">#C0C9A1</span>
  <span class="swatch-code" style="left:686px">#C0C9A1</span>
</header>

<span class="view-label" style="left:66px">FRONT</span>
<span class="view-label" style="left:612px">BACK</span>

<section class="pouch pouch-front" style="left:69px">
  <svg class="pouch-frame" viewBox="0 0 517 793" width="517" height="793">
    <g fill="none" stroke="#eef0dc" stroke-width="1">
      <path d="M21 0 V637 Q258 900 496 637 V0"/>
      <path d="M0 69 H517 M0 87 H517 M0 121 H517" stroke-dasharray="6 4"/>
      <path d="M0 102 H517 M0 106 H517"/>
    </g>
    <circle cx="258" cy="34" r="14" fill="#92999d" stroke="#eef0dc"/>
    <path d="M0 64 L10 69 L0 74Z M517 64 L507 69 L517 74Z" fill="#92999d" stroke="#eef0dc"/>
  </svg>
  <div class="tagline">
    <div class="tag-item"><div class="tag-simple">SIMPLE</div></div>
    <div class="tag-item"><div class="tag-big">HEALTHY</div><div class="tag-small">INGREDIENTS</div></div>
    <div class="tag-item"><div class="tag-big">EARTH FRIENDLY</div><div class="tag-small">PACKAGING</div></div>
  </div>
  <div class="label-window"></div>
  <div class="free-from">
    <div class="free-item">
      <svg class="free-icon" width="32" height="36" viewBox="0 0 32 36" fill="none" stroke="#5a9190" stroke-width="1.8" stroke-linecap="round" role="img" aria-label="No corn icon">
        <ellipse cx="16" cy="15" rx="5.5" ry="10" fill="#5a9190" fill-opacity=".35"/>
        <path d="M16 34 C8 30 5 22 7 14 M16 34 C24 30 27 22 25 14"/>
        <path d="M4 4 L28 32"/>
      </svg>NO<br>CORN
    </div>
    <div class="free-item">
      <svg class="free-icon" width="32" height="36" viewBox="0 0 32 36" fill="none" stroke="#5a9190" stroke-width="1.8" stroke-linecap="round" role="img" aria-label="No wheat icon">
        <path d="M16 35 V6"/>
        <path d="M16 12 Q10 10 10 5 Q15 6 16 12 M16 12 Q22 10 22 5 Q17 6 16 12 M16 20 Q10 18 10 13 Q15 14 16 20 M16 20 Q22 18 22 13 Q17 14 16 20 M16 28 Q10 26 10 21 Q15 22 16 28 M16 28 Q22 26 22 21 Q17 22 16 28" fill="#5a9190" fill-opacity=".35"/>
        <path d="M4 4 L28 32"/>
      </svg>NO<br>WHEAT
    </div>
    <div class="free-item">
      <svg class="free-icon" width="32" height="36" viewBox="0 0 32 36" fill="#5a9190" stroke="#5a9190" stroke-width="1.8" stroke-linecap="round" role="img" aria-label="No soy icon">
        <ellipse cx="11" cy="16" rx="7" ry="6" fill-opacity=".75" stroke="none"/>
        <ellipse cx="22" cy="21" rx="7" ry="6" fill-opacity=".75" stroke="none"/>
        <path d="M4 4 L28 32" fill="none" stroke="#c0c9a1" stroke-width="4"/>
        <path d="M4 4 L28 32" fill="none"/>
      </svg>NO<br>SOY
    </div>
    <div class="free-item">
      <svg class="free-icon" width="32" height="36" viewBox="0 0 32 36" fill="none" stroke="#5a9190" stroke-width="1.8" stroke-linecap="round" role="img" aria-label="No GMO icon">
        <path d="M9 4 C9 14 23 14 23 22 C23 28 9 28 9 34"/>
        <path d="M23 4 C23 14 9 14 9 22 C9 28 23 28 23 34"/>
        <path d="M11 9 H21 M12 27 H20"/>
        <path d="M4 4 L28 32"/>
      </svg>NO<br>GMO
    </div>
  </div>
</section>

<section class="pouch pouch-back" style="left:614px">
  <svg class="pouch-frame" viewBox="0 0 517 793" width="517" height="793">
    <g fill="none" stroke="#eef0dc" stroke-width="1">
      <path d="M21 0 V637 Q258 900 496 637 V0"/>
      <path d="M0 69 H517 M0 87 H517 M0 121 H517" stroke-dasharray="6 4"/>
      <path d="M0 102 H517 M0 106 H517"/>
    </g>
    <circle cx="258" cy="34" r="14" fill="#92999d" stroke="#eef0dc"/>
    <path d="M0 64 L10 69 L0 74Z M517 64 L507 69 L517 74Z" fill="#92999d" stroke="#eef0dc"/>
  </svg>
  <div class="recipes-head">OUR<br>RECIPES</div>
  <ul class="recipe-list">
    <li class="recipe">
      <svg class="recipe-icon" viewBox="0 0 38 32" role="img" aria-label="Leaf icon">
        <path d="M10 28 C8 14 20 6 34 6 C34 20 24 30 10 28Z" fill="#5a9190"/>
        <path d="M10 28 L26 12" stroke="#c0c9a1" stroke-width="1.5" fill="none"/>
        <path d="M6 4 V10 M3 7 H9" stroke="#5a9190" stroke-width="1.3"/>
      </svg>CLEAN &amp; SIMPLE
    </li>
    <li class="recipe">
      <svg class="recipe-icon" viewBox="0 0 38 32" fill="none" stroke="#5a9190" stroke-width="1.8" stroke-linecap="round" role="img" aria-label="No artificial ingredients flask icon">
        <path d="M14 3 H24 M16 3 V12 L8 28 H30 L22 12 V3"/>
        <path d="M11 22 H27 L30 28 H8Z" fill="#5a9190"/>
        <path d="M6 2 L32 30"/>
      </svg>NOTHING ARTIFICIAL
    </li>
    <li class="recipe">
      <svg class="recipe-icon" viewBox="0 0 38 32" fill="none" stroke="#5a9190" stroke-width="1.8" stroke-linecap="round" role="img" aria-label="Hands holding a jar icon">
        <rect x="13" y="4" width="12" height="15" rx="3" fill="#5a9190" fill-opacity=".6"/>
        <path d="M12 4 H26"/>
        <path d="M4 10 C3 20 10 24 16 28 M34 10 C35 20 28 24 22 28"/>
      </svg>HANDCRAFTED IN<br>SMALL BATCHES
    </li>
    <li class="recipe">
      <svg class="recipe-icon" viewBox="0 0 38 32" role="img" aria-label="Mountains and water icon">
        <path d="M2 22 L14 8 L20 15 L26 9 L36 22Z" fill="#5a9190"/>
        <path d="M2 26 Q10 22 18 26 T36 26" stroke="#5a9190" stroke-width="1.8" fill="none"/>
      </svg>PREMIUM INGREDIENTS<br>FROM THE PACIFIC NW
    </li>
  </ul>
  <div class="brand-name"><span class="brand-dot"></span><span>Meadowlark<br>Treat Kitchen</span></div>
  <div class="badge badge-eco" role="img" aria-label="Eco-friendly materials and practices stamp"></div>
  <div class="badge badge-origin" role="img" aria-label="Hand made in the Pacific Northwest stamp with mountain, forest and wave scene"></div>
  <div class="contact">Cedar Hollow, WA | 866-555-0142<br>hello@meadowlarktreats.com<br>www.meadowlarktreats.com</div>
  <p class="eco-copy">We reduce our carbon footprint through responsibly sourced ingredients,<br>efficient production, and packaging optimized to reduce material use and<br>transportation impact. By working with regional suppliers and minimizing<br>waste, we help lower emissions while protecting the natural environment<br>share with our dogs.</p>
  <div class="compost"><div class="compost-big">COMPOSTABLE</div><div class="compost-small">PACKAGING</div></div>
</section>
</body>
</html>
```